Darin Wekel Orthodontics
Business Card, Letterhead, Envelopes, Folder
@ Project holder : Please,Extend this Contest.
I am interested and Coming....
Anyone do a full size envelope where the letterhead slides in the envelope unfolded.
Anyone willing to experiment by putting the log and info at the bottom of the stationary page rather than the top.
Thanks for your submissions.#2,3,6,7 appear too busy for me. Lets stick with simplicity. Back of business card should probably have a white or light background so we can write the appoitment time in pen on the card.
ai format uploaded
kindly upload ai or eps file of logo

```html
<!DOCTYPE html>
<html lang="en">
<head>
<meta charset="utf-8">
<title>Darin Wekel Orthodontics – Letterhead</title>
<link rel="stylesheet" href="https://fonts.googleapis.com/css2?family=Montserrat:wght@400;500&display=swap">
<style>
  :root {
    --backdrop: #ece9e4;
    --paper: #ffffff;
    --brand-blue: #1e8fcf;
    --ink: #5a5f66;
    --ink-soft: #8a9097;
  }
  * { margin: 0; padding: 0; box-sizing: border-box; }
  html, body {
    width: 1200px;
    height: 749px;
    overflow: hidden;
    background: var(--backdrop);
    font-family: "Montserrat", sans-serif;
  }
  .canvas {
    position: relative;
    width: 1200px;
    height: 749px;
  }
  .letterhead {
    position: absolute;
    left: 337px;
    top: 30px;
    width: 526px;
    height: 690px;
    background: var(--paper);
    box-shadow: 0 6px 22px rgba(0, 0, 0, 0.18);
  }
  .brand {
    position: absolute;
    left: 34px;
    bottom: 44px;
    color: var(--brand-blue);
    display: flex;
    align-items: center;
    gap: 7px;
  }
  .brand-dot {
    width: 9px;
    height: 9px;
    border-radius: 50%;
    background: var(--brand-blue);
  }
  .brand-text {
    display: flex;
    flex-direction: column;
    line-height: 1.1;
  }
  .brand-name {
    font-size: 20px;
    font-weight: 500;
    letter-spacing: 0.5px;
  }
  .brand-sub {
    font-size: 8px;
    font-weight: 500;
    letter-spacing: 1.2px;
    text-transform: lowercase;
  }
  .contact {
    position: absolute;
    right: 30px;
    bottom: 40px;
    text-align: right;
    font-size: 5.5px;
    line-height: 1.55;
    color: var(--ink);
  }
  .contact .contact-name { font-weight: 500; color: var(--ink); }
  .contact-bar {
    position: absolute;
    right: 14px;
    bottom: 58px;
    width: 9px;
    height: 34px;
    background: var(--brand-blue);
  }
</style>
</head>
<body>
  <main class="canvas">
    <section class="letterhead" aria-label="Darin Wekel Orthodontics letterhead">
      <div class="brand">
        <span class="brand-dot" aria-hidden="true"></span>
        <div class="brand-text">
          <span class="brand-name">Darin Wekel</span>
          <span class="brand-sub">Orthodontics</span>
        </div>
      </div>
      <address class="contact">
        <div class="contact-name">Darin Wekel</div>
        <div>410 Harbor Lane Suite 2</div>
        <div>Riverton, ST 00000</div>
        <div>Phone: 555 0142 0198</div>
        <div>www.darinwekel.com</div>
      </address>
      <div class="contact-bar" aria-hidden="true"></div>
    </section>
  </main>
</body>
</html>
```